automatic Real Estate Sales Brochure

Print-out of 3 to 8 pages automatically on a color inkjet printer. Page size A4
All details for my Real Estate Sales Design Project are in attached file.
Here some points:
We have abound 100 real estate objects for sale (houses, flats and pieces of land).
For each item, our system creates automatically a sales documentation, which we print out and hand to the potential buyers after they've visited the object or send it by mail upon request in form of a pdf.
This document should be of 3 to maximum 8 pages.
It should be of a modern design and invite the client to read it.
The information should be clear and quick to find.
If the global look could somehow relate to the look of our web site www.velorancasa.ch, that would be nice.
The company data is there for legal reasons, but it is the agent's phone and mail that the clients should use for contact.
The photos should be of big size (2 by page?) without being distorted nor cut.
Optionally, to save ink and pages, maybe only the first 3-4 photos full size and the rest smaller?

Target Market(s)

will be printed or sent as PDF "on the fly", meaning no pre-printing at a print shop!

Industry/Entity Type

Real Estate

Font styles to use
Sans Serif

Requirements
Must have
• see details in attached file
Should not have
• no edge-to-edge printing
• no double-page printing (A3)

```html
<!DOCTYPE html>
<html lang="fr">
<head>
<meta charset="utf-8">
<title>VeloranCasa – Brochure de vente</title>
<link href="https://fonts.googleapis.com/css2?family=Open+Sans:wght@400;600;700&display=swap" rel="stylesheet">
<style>
:root{
  --backdrop:#c4c4c4;
  --paper:#ffffff;
  --brand-red:#e31e24;
  --brand-cyan:#1ab7ea;
  --ink:#222222;
  --muted:#555555;
  --row-grey:#e2e2e2;
  --band-grey:#ececec;
}
*{box-sizing:border-box;margin:0;padding:0}
html,body{width:1200px;height:960px;overflow:hidden;background:var(--backdrop)}
body{font-family:"Open Sans",sans-serif;color:var(--ink)}
.canvas{position:relative;width:1200px;height:960px;overflow:hidden}
.page{position:absolute;background:var(--paper);box-shadow:2px 3px 4px rgba(0,0,0,.35);overflow:hidden}
.page-label{position:absolute;font-size:27px;letter-spacing:1px;transform:translateX(-50%);white-space:nowrap}
.abs{position:absolute}
.brand{position:absolute;left:0;right:0;text-align:center;font-weight:700;color:var(--brand-red);letter-spacing:.5px;line-height:1}
.photo{position:absolute}
.photo--garden{background:linear-gradient(180deg,#dbe9f2 0%,#8fb06a 30%,#4f7e2f 60%,#2f5a1e 100%)}
.photo--room{background:linear-gradient(180deg,#eeeae4 0%,#e4ddd2 50%,#c07a3a 72%,#8e4f1e 100%)}
.photo--bright{background:linear-gradient(180deg,#f3f1ec 0%,#e8e2d6 55%,#c98a45 80%,#9a5a24 100%)}
.photo--bath{background:linear-gradient(180deg,#eef0f2 0%,#d7dbe0 60%,#b9c0c8 100%)}
.photo--dark{background:linear-gradient(90deg,#f0e9da 0%,#e6d9bf 35%,#222 40%,#111 100%)}
.photo--portrait{background:linear-gradient(180deg,#d9d9d9 0%,#b3b3b3 100%)}
.tab{position:absolute;left:0;background:var(--brand-cyan);color:var(--ink);padding-left:28px;display:flex;align-items:center}
.icon{display:inline-block;width:7px;height:7px;border-radius:50%;background:var(--ink);vertical-align:middle;margin-right:4px}
/* page 1 */
.cover-tagline{left:0;right:0;top:75px;text-align:center;color:var(--brand-cyan);font-size:16px;letter-spacing:.5px}
.cover-title{left:0;right:0;top:113px;text-align:center;color:var(--brand-red);font-size:17px;letter-spacing:.5px}
.location-band{position:absolute;left:0;right:0;top:455px;height:15px;background:var(--brand-cyan)}
.location-band span{position:absolute;left:50%;top:-2px;transform:translateX(-50%);background:var(--paper);color:var(--brand-red);font-size:14px;padding:0 8px;letter-spacing:.5px;line-height:19px}
.facts{position:absolute;left:110px;top:480px;list-style:none;font-size:12px;letter-spacing:.4px}
.facts li{height:15.7px;display:flex;align-items:center}
.facts .dot{width:9px;height:9px;border-radius:50%;background:var(--brand-cyan);margin-right:4px}
.facts .label{width:124px;color:var(--muted)}
.facts .value{color:var(--brand-red)}
/* page 2 */
.description{position:absolute;left:28px;top:71px;width:254px;font-size:6.3px;line-height:10.4px;text-align:justify}
.description p{margin-bottom:10.4px}
.description .spacer{float:right;width:86px;height:130px}
.agent-name{position:absolute;left:198px;width:90px;top:156px;text-align:center;font-size:11px}
.agent-line{position:absolute;left:198px;width:90px;text-align:center;font-size:6px;color:var(--muted)}
.contact-footer{position:absolute;left:0;right:0;top:401px;height:23px;background:#cfcfcf}
.contact-footer .inner{position:absolute;left:22px;right:18px;top:0;bottom:0;background:var(--paper);display:flex;justify-content:space-around;align-items:center;font-size:6.3px;color:var(--brand-red);line-height:10.5px}
/* page 3 */
.contact-band{position:absolute;left:0;right:0;top:39px;height:23px;background:var(--band-grey);display:flex;justify-content:space-around;align-items:center;font-size:6.3px;color:var(--brand-red);line-height:10.5px;padding:0 20px}
.specs{position:absolute;left:26px;top:96px;width:262px;list-style:none;font-size:8.6px;line-height:10.5px}
.specs li{display:flex;align-items:center;height:10.5px}
.specs .dot{width:7px;height:7px;border-radius:50%;background:var(--brand-cyan);margin-right:7px}
.specs .label{width:115px;color:var(--brand-red);background:var(--row-grey);padding-left:3px;margin-right:2px}
.specs .value{flex:1;color:var(--muted);background:var(--row-grey);padding-left:3px}
.specs li:nth-child(even) .label,.specs li:nth-child(even) .value{background:var(--paper)}
/* page 4 */
.mini-contacts{position:absolute;left:20px;top:36px;width:150px;display:flex;justify-content:space-between;font-size:5px;line-height:8.7px}
.mini-contacts .icon{width:5px;height:5px;margin-right:2px}
.situation{position:absolute;left:26px;top:96px;width:134px;font-size:6.4px;line-height:10.4px;text-align:justify}
/* presentation caption */
.caption-title{position:absolute;left:56px;top:784px;font-size:40px;letter-spacing:2px}
.caption-sub{position:absolute;left:50px;top:832px;font-size:26px;letter-spacing:1.5px}
.caption-brand{position:absolute;left:56px;top:868px;font-size:54px;font-weight:700;color:var(--brand-red)}
</style>
</head>
<body>
<main class="canvas">

  <!-- Page 1 : cover -->
  <section class="page" style="left:46px;top:33px;width:438px;height:618px">
    <div class="brand" style="top:30px;font-size:30px">VeloranCasa</div>
    <p class="abs cover-tagline">Spécialiste romand de vente immobilière</p>
    <h1 class="abs cover-title" style="font-weight:400">Lumineux 4.5 de 100m2 idéalement situé</h1>
    <div class="photo photo--garden" role="img" aria-label="Jardin arboré devant l'immeuble" style="left:0;top:119px;width:438px;height:331px"></div>
    <div class="location-band"><span>1200 Genève</span></div>
    <div class="photo photo--dark" role="img" aria-label="Séjour avec armoire encastrée" style="left:0;top:477px;width:100px;height:66px"></div>
    <div class="photo photo--bright" role="img" aria-label="Couloir d'entrée" style="left:0;top:545px;width:100px;height:64px"></div>
    <div class="photo photo--bright" role="img" aria-label="Chambre lumineuse" style="left:338px;top:477px;width:100px;height:66px"></div>
    <div class="photo photo--room" role="img" aria-label="Cuisine équipée" style="left:338px;top:545px;width:100px;height:64px"></div>
    <ul class="facts">
      <li><span class="dot"></span><span class="label">Type de bien</span><span class="value">Appartement</span></li>
      <li><span class="dot"></span><span class="label">Surface habitable</span><span class="value">100 m²</span></li>
      <li><span class="dot"></span><span class="label">Nombre de pièces</span><span class="value">4.5</span></li>
      <li><span class="dot"></span><span class="label">Surface parcelle</span><span class="value">1'000 m²</span></li>
      <li><span class="dot"></span><span class="label">Prix</span><span class="value">910'000.-</span></li>
      <li><span class="dot"></span><span class="label">Année</span><span class="value">1994</span></li>
      <li><span class="dot"></span><span class="label">Etat</span><span class="value">Bon état</span></li>
      <li><span class="dot"></span><span class="label">Disponible</span><span class="value">1.1.2018</span></li>
    </ul>
  </section>
  <div class="page-label" style="left:266px;top:653px">Page 1</div>

  <!-- Page 2 : description -->
  <section class="page" style="left:504px;top:30px;width:306px;height:434px">
    <div class="brand" style="top:15px;font-size:22px">VeloranCasa</div>
    <div class="tab" style="top:48px;width:98px;height:15px;font-size:11px">Description</div>
    <div class="photo photo--portrait" role="img" aria-label="Portrait de la courtière" style="left:200px;top:48px;width:84px;height:108px;border:2px solid #ddd"></div>
    <div class="agent-name">Claire Morand</div>
    <div class="agent-line" style="top:171px">morand@velorancasa.ch</div>
    <div class="agent-line" style="top:180px">077 555 01 23</div>
    <div class="description">
      <div class="spacer"></div>
      <p>Venez visiter sans tarder ce bel appartement situé dans un environnement calme et vert tout en étant proche du centre-ville et de toutes les commodités. Il profite de beaux volumes et de pièces de vie très lumineuses. Au 1er étage d'une copropriété soignée, c'est le bien idéal pour un couple ou une famille.</p>
      <p>Cet appartement pourrait aussi convenir comme investissement pour un client souhaitant le louer.<br>Il est en bon état d'entretien et se réjouit d'accueillir ses nouveaux propriétaires !</p>
      <p>Il se distribue ainsi :</p>
      <p>Une entrée avec armoire encastrée desserre de part et d'autre la partie jour et la partie nuit. La spacieuse pièce de vie se compose d'une cuisine ouverte entièrement équipée et aménagée s'ouvrant sur le séjour. Il profite d'une exposition optimale. Du séjour, vous avez accès à un agréable balcon qui offre une belle vue dégagée sur un environnement verdoyant.</p>
      <p>La partie nuit offre trois belles chambres, une salle de bains avec baignoire, lavabo, wc ainsi qu'un wc visiteurs.<br>Deux places de parc intérieures en sus s'ajoutent à ce bel appartement !</p>
      <p>N'hésitez pas, contactez-moi pour plus d'informations et pour une visite !</p>
    </div>
    <footer class="contact-footer">
      <div class="inner">
        <div><span class="icon"></span>VeloranCasa Sàrl<br><span style="margin-left:11px">1899 Montclair</span></div>
        <div><span class="icon"></span>www.velorancasa.ch<br><span class="icon"></span>info@velorancasa.ch</div>
        <div><span class="icon"></span>Tél. 021 555 40 10<br><span class="icon"></span>Fax. 021 555 40 11</div>
      </div>
    </footer>
  </section>
  <div class="page-label" style="left:660px;top:468px">Page 2</div>

  <!-- Page 3 : caractéristiques -->
  <section class="page" style="left:822px;top:30px;width:306px;height:434px">
    <div class="brand" style="top:14px;font-size:22px">VeloranCasa</div>
    <div class="contact-band">
      <div><span class="icon"></span>VeloranCasa Sàrl<br><span style="margin-left:11px">1899 Montclair</span></div>
      <div><span class="icon"></span>www.velorancasa.ch<br><span class="icon"></span>info@velorancasa.ch</div>
      <div><span class="icon"></span>Tél. 021 555 40 10<br><span class="icon"></span>Fax. 021 555 40 11</div>
    </div>
    <div class="tab" style="top:71px;width:128px;height:16px;font-size:10px;padding-left:40px">Caractéristiques</div>
    <ul class="specs">
      <li><span class="dot"></span><span class="label">Etage</span><span class="value">1er étage</span></li>
      <li><span class="dot"></span><span class="label">Vue</span><span class="value">vue dégagée sur le parc</span></li>
      <li><span class="dot"></span><span class="label">Commerces</span><span class="value">à proximité immédiate</span></li>
      <li><span class="dot"></span><span class="label">Ecoles</span><span class="value">Collège des Tilleuls</span></li>
      <li><span class="dot"></span><span class="label">Transport public</span><span class="value">à 5 minutes à pied</span></li>
      <li><span class="dot"></span><span class="label">Chauffage</span><span class="value">mazout / au sol</span></li>
      <li><span class="dot"></span><span class="label">Cave</span><span class="value">oui</span></li>
      <li><span class="dot"></span><span class="label">Garage</span><span class="value">2 places de parc intérieures</span></li>
      <li><span class="dot"></span><span class="label">Balcon</span><span class="value">oui</span></li>
      <li><span class="dot"></span><span class="label">Ascenseur</span><span class="value">oui</span></li>
    </ul>
    <div class="photo photo--room" role="img" aria-label="Séjour avec cuisine ouverte et parquet" style="left:0;top:204px;width:306px;height:230px"></div>
  </section>
  <div class="page-label" style="left:974px;top:461px">Page 3</div>

  <!-- Page 4 : situation -->
  <section class="page" style="left:822px;top:494px;width:306px;height:433px">
    <div class="brand" style="top:12px;font-size:20px;right:auto;left:20px;width:140px">VeloranCasa</div>
    <div class="mini-contacts">
      <div><span class="icon"></span>VeloranCasa Sàrl<br><span style="margin-left:7px">1899 Montclair</span><br><span class="icon"></span>www.velorancasa.ch</div>
      <div><span class="icon"></span>Tél. 021 555 40 10<br><span class="icon"></span>Fax. 021 555 40 11<br><span class="icon"></span>info@velorancasa.ch</div>
    </div>
    <div class="tab" style="top:71px;width:82px;height:15px;font-size:11px;padding-left:26px">Situation</div>
    <p class="situation">Cet appartement a l'avantage de se situer proche de toutes les commodités, à 3 minutes du Collège des Tilleuls, à 1 minute de l'arrêt de bus et à 3 minutes des axes autoroutiers. Vous rejoindrez le centre-ville en 7 minutes. Des atouts que vous saurez apprécier.</p>
    <div class="photo photo--bright" role="img" aria-label="Chambre avec porte-fenêtre" style="left:174px;top:0;width:132px;height:100px"></div>
    <div class="photo photo--bright" role="img" aria-label="Couloir et portes" style="left:174px;top:108px;width:132px;height:99px"></div>
    <div class="photo photo--bath" role="img" aria-label="Salle de bains" style="left:174px;top:216px;width:132px;height:98px"></div>
    <div class="photo photo--room" role="img" aria-label="Cuisine" style="left:174px;top:322px;width:56px;height:100px"></div>
    <div class="photo photo--bright" role="img" aria-label="Armoire d'entrée" style="left:234px;top:322px;width:72px;height:100px"></div>
    <div class="photo photo--bright" role="img" aria-label="Séjour lumineux" style="left:0;top:196px;width:164px;height:109px"></div>
    <div class="photo photo--dark" role="img" aria-label="Chambre avec armoire" style="left:0;top:314px;width:164px;height:109px"></div>
  </section>
  <div class="page-label" style="left:974px;top:921px">Page 4</div>

  <h2 class="caption-title" style="font-weight:400">Brochure Design</h2>
  <p class="caption-sub">4 Pages - Page Size: A4</p>
  <p class="caption-brand">VeloranCasa</p>

</main>
</body>
</html>
```